Luxury Candle Startup Needs Modern Packaging Box & Matching Label Design

We are Lunavale, a luxury candle company about to launch in Australia and we need a box packaging design that is modern, minimalist, and feminine. Our target audience are females, mostly mothers, within the age range of 25-45 who are looking for high quality, handmade luxurious products. Our company is going to have a large social media presence with new mothers as we are going to show our journey with starting a business whilst on maternity leave. We would like the arch shape incorporated into the box packaging as it is beautiful and symbolises moving into a new phase in life which really represents the brand. We would like for the packaging box to be a simple white box with a sleeve insert over the box with the design to make printing easier. Our colour inspiration are very earthy colours and would like the sleeve colour to be easily changed according to the scent. For example dusky rose coloured sleeve for rose patchouli and amber scent, light coffee coloured sleeve for coffee bean cacao scent etc. Please see uploaded files for inspiration, our logo, and the type of candle jars used.
The box dimensions are:
External Dimension: 95mmW x 95mmL x 116mmH
We look forward to seeing your amazing designs!

```html
<!DOCTYPE html>
<html lang="en">
<head>
<meta charset="utf-8">
<title>Lunavale – Coffee Bean Cacao Packaging</title>
<link rel="stylesheet" href="https://fonts.googleapis.com/css2?family=Jost:wght@300;400;500&display=swap">
<style>
  :root {
    --canvas: #f2f2f2;
    --sleeve: #ddd0b4;
    --art-light: #d3c3a1;
    --art-deep: #bfa97f;
    --ink: #7a5c4a;
    --ink-soft: #8a6d5a;
  }
  * { box-sizing: border-box; margin: 0; padding: 0; }
  html, body { width: 1200px; height: 1200px; overflow: hidden; }
  body {
    position: relative;
    background: var(--canvas);
    font-family: "Jost", sans-serif;
    color: var(--ink);
  }

  .wordmark {
    font-family: "Jost", sans-serif;
    font-weight: 400;
    color: var(--ink);
    text-transform: uppercase;
    line-height: 1;
    text-align: center;
    white-space: nowrap;
  }
  .tagline {
    font-weight: 500;
    text-transform: uppercase;
    text-align: center;
    color: var(--ink);
    line-height: 1;
    white-space: nowrap;
  }
  .tagline .country { display: block; }
  .scent-name {
    font-weight: 300;
    text-transform: uppercase;
    text-align: center;
    color: var(--ink-soft);
    line-height: 1;
    white-space: nowrap;
  }
  .botanical {
    background: radial-gradient(ellipse at 50% 55%, var(--art-deep) 0%, var(--art-light) 70%, var(--art-light) 100%);
  }

  /* Sleeve front panel, flat */
  .sleeve {
    position: absolute;
    left: 420px; top: 300px;
    width: 400px; height: 470px;
    background: var(--sleeve);
    display: flex; flex-direction: column; align-items: center;
    padding-top: 92px;
  }
  .sleeve .wordmark { font-size: 38px; letter-spacing: 5px; }
  .sleeve .tagline { margin-top: 14px; font-size: 9px; letter-spacing: 1.4px; }
  .sleeve .tagline .country { margin-top: 6px; font-size: 7px; letter-spacing: 1.4px; }
  .sleeve .botanical {
    margin-top: 20px;
    width: 170px; height: 190px;
    border-radius: 85px 85px 0 0;
  }
  .sleeve .scent-name { margin-top: 24px; font-size: 16px; letter-spacing: 0.4px; }

  /* Arch label */
  .arch-label {
    position: absolute;
    left: 1003px; top: 545px;
    width: 158px; height: 290px;
    background: var(--sleeve);
    border-radius: 79px 79px 0 0;
    display: flex; flex-direction: column; align-items: center;
    padding-top: 44px;
  }
  .arch-label .botanical {
    width: 120px; height: 180px;
    border-radius: 60px 60px 0 0;
  }
  .arch-label .wordmark { margin-top: 14px; font-size: 19px; letter-spacing: 2px; }
  .arch-label .tagline { margin-top: 8px; font-size: 8px; letter-spacing: 1.2px; }
  .arch-label .tagline .country { margin-top: 6px; font-size: 6.5px; letter-spacing: 1.2px; }

  /* Brand band */
  .brand-band {
    position: absolute;
    left: 0; top: 872px;
    width: 1200px; height: 328px;
    background: var(--sleeve);
    display: flex; flex-direction: column; align-items: center;
    padding-top: 96px;
  }
  .brand-band .wordmark { font-size: 46px; letter-spacing: 9px; }
  .brand-band .tagline { margin-top: 20px; font-size: 10px; letter-spacing: 2px; }
  .brand-band .tagline .country { margin-top: 8px; font-size: 8.5px; letter-spacing: 1.8px; }
  .brand-band .scent-name { margin-top: 18px; font-size: 21px; letter-spacing: 0.8px; }
</style>
</head>
<body>

  <section class="sleeve" aria-label="Box sleeve, front panel">
    <h1 class="wordmark">Lunavale</h1>
    <p class="tagline">Luxury Fragrance<span class="country">Australia</span></p>
    <div class="botanical" role="img" aria-label="Line illustration of cacao pods, leaves and blossoms"></div>
    <p class="scent-name">Coffee Bean Cacao</p>
  </section>

  <section class="arch-label" aria-label="Arch-shaped jar label">
    <div class="botanical" role="img" aria-label="Line illustration of cacao blossoms, leaf and pod"></div>
    <p class="wordmark">Lunavale</p>
    <p class="tagline">Luxury Fragrance<span class="country">Australia</span></p>
  </section>

  <footer class="brand-band">
    <p class="wordmark">Lunavale</p>
    <p class="tagline">Luxury Fragrance<span class="country">Australia</span></p>
    <p class="scent-name">Coffee Bean Cacao</p>
  </footer>

</body>
</html>
```